quorvelbank.com

Design proposals for a gold bank site and gold wallet main page. The site will let people (and companies) open accounts and purchase gold for deposit and later make payments with the gold they hold in the bank. The bank will be a e-money licensed venture located in Switzerland. The functionality of the "system" will be very simple and possibly only use icon symbols so it can be multilingual.

The mainstays of the site will be security and trust. Al digital gold is backed 100 % by visible gold in vault audited every day.

Target Market(s)

Asian and American gold buyers and people preferring gold to currency

Industry/Entity Type

Security

Requirements
Must have
• a) Logo
b) Main index page with a new logo and design
c) System (post log in e-wallet) main page showing the last transactions of the client and give client options to transfer funds and make deposits
Nice to have
• sample contact form
sample faq page
terms page design
Should not have
• So much text since it will be aimed at the worldwide market

```html
<!DOCTYPE html>
<html lang="en">
<head>
<meta charset="utf-8">
<title>Quorvelbank</title>
<link rel="stylesheet" href="https://fonts.googleapis.com/css2?family=Ubuntu:wght@300;400;500;700&family=Arimo:wght@400&display=swap">
<style>
:root{
  --page:#eeece7;
  --ink:#222;
  --body:#4a4a4a;
  --muted:#7a7a7a;
  --gold:#f5c314;
  --gold-deep:#e8a800;
  --gold-text:#f2c200;
  --dark:#1c1c1c;
  --darker:#111;
  --link:#1b78b5;
  --footer:#2a2a2a;
  --rule:#d9d6cf;
}
*{margin:0;padding:0;box-sizing:border-box}
html,body{width:1200px;height:1078px;overflow:hidden;background:var(--page)}
body{position:relative;font-family:"Ubuntu",sans-serif;color:var(--ink)}
.abs{position:absolute}

/* header */
.brand{left:173px;top:32px;display:flex;align-items:center;gap:12px}
.brand-mark{width:50px;height:50px;border-radius:50%;background:var(--gold)}
.brand-name{font-size:34px;font-weight:500;color:#2b2b2b;letter-spacing:-.5px}
.join{left:771px;top:22px;width:136px;height:21px;border-radius:11px;background:linear-gradient(#b8b8b8,#8f8f8f);color:#fff;font-size:12px;line-height:21px;padding-left:13px}
.join::after{content:"";position:absolute;right:5px;top:3px;width:15px;height:15px;border-radius:50%;background:#555}
.join-arrow{right:10px;top:7px;width:5px;height:5px;border-top:2px solid #fff;border-right:2px solid #fff;transform:rotate(45deg);z-index:1}
.social{top:20px;display:flex;gap:5px;left:914px}
.social span{width:23px;height:23px;border-radius:3px;background:#cfcfcf}
.social span:nth-child(4){background:#f08a24}
.nav-rule{left:564px;top:60px;width:456px;border-top:1px solid var(--rule)}
.nav{left:564px;top:70px;display:flex;align-items:center;font-size:14px;color:#333}
.nav a{color:inherit;text-decoration:none;margin-right:25px}
.nav a.current{background:var(--darker);color:#fff;font-weight:500;padding:5px 10px;margin-right:13px;font-size:14.5px}

/* hero */
.hero{left:87px;top:111px;width:1038px;height:400px;background:var(--dark);overflow:hidden}
.hero-art{right:92px;top:37px;width:360px;height:270px;background:radial-gradient(ellipse at 55% 50%,#f7d25a 0%,#d9a21c 45%,rgba(28,28,28,0) 72%)}
.hero-title{left:165px;top:172px;font-size:42px;font-weight:500;color:#fff;letter-spacing:-1.2px}
.hero-points{left:166px;top:239px;font-size:15px;font-weight:300;line-height:26px;color:var(--gold-text)}
.pay{left:162px;top:325px;width:295px;height:76px;border-radius:4px;background:#252525}
.pay-thumb{left:10px;top:9px;width:89px;height:59px;background:linear-gradient(135deg,#fff 0%,#e9c14a 45%,#b9861a 70%,#fff 100%);border:2px solid #fff}
.pay-small{left:108px;top:12px;font-size:12px;color:#fff}
.pay-big{left:108px;top:29px;font-size:14px;font-weight:500;color:#fff}
.pay-links{left:108px;top:57px;font-size:11px;color:var(--gold-text);word-spacing:1px}
.pay-go{left:272px;top:29px;width:22px;height:22px;border-radius:50%;background:#3e3e3e}
.pay-go::after{content:"";position:absolute;left:6px;top:7px;width:6px;height:6px;border-top:2px solid #fff;border-right:2px solid #fff;transform:rotate(45deg)}
.arc{left:0;top:360px;width:1200px;height:180px}

/* about */
.about-title{left:0;top:490px;width:1200px;text-align:center;font-size:30px;font-weight:300;color:var(--gold-deep)}
.about-text{left:160px;width:880px;text-align:center;font-size:12.5px;line-height:16px;color:var(--body);font-weight:300}
.cta{left:519px;top:644px;width:161px;height:31px;border-radius:6px;background:linear-gradient(#ffe45a,#f3b50b);box-shadow:0 1px 0 #d7a000;font-size:13px;line-height:31px;text-align:center;color:#3a2a00;font-weight:500}
.divider{left:148px;top:660px;width:902px;border-top:1px solid var(--rule);z-index:-1}

/* features */
.feat-bar{left:158px;top:708px;width:596px;height:26px;background:var(--darker);color:#fff;font-size:12px;line-height:26px;padding-left:6px}
.feat-pager{right:20px;top:9px;display:flex;gap:10px;align-items:center}
.feat-pager i{width:9px;height:9px;background:#444}
.feat-pager i.on{background:var(--gold)}
.feat-pager b{width:0;height:0;border-top:4px solid transparent;border-bottom:4px solid transparent;border-right:5px solid #fff;margin-right:2px}
.card{top:743px;width:181px}
.card-img{width:181px;height:90px}
.card h3{margin-top:15px;font-size:13px;font-weight:400;line-height:17px;color:var(--link)}
.card p{margin-top:10px;font-family:"Arimo",sans-serif;font-size:10.5px;line-height:16.6px;color:var(--muted)}

/* side boxes */
.promo{left:781px;top:707px;width:252px;height:126px;background:var(--darker)}
.promo h4{position:absolute;left:8px;top:12px;font-size:25px;font-weight:700;color:#fff;letter-spacing:-.3px}
.promo .offer{left:8px;top:44px;font-size:15px;font-weight:700;color:var(--gold-text)}
.promo .note{left:8px;top:67px;font-family:"Arimo",sans-serif;font-size:10px;line-height:13px;color:#aaa}
.promo .more{left:8px;top:108px;font-size:11.5px;color:#ddd;text-decoration:underline}
.promo-art{left:160px;top:45px;width:79px;height:79px;background:linear-gradient(160deg,#ddd,#8a8a8a 60%,#3a3a3a)}
.wallet{left:781px;top:843px;width:252px;height:137px;background:linear-gradient(#f7f7f7,#dedede);border:1px solid #ccc;border-radius:2px}
.wallet-head{height:34px;background:var(--darker);color:#fff;font-size:17px;line-height:34px;padding-left:11px;border-bottom:2px solid #999}
.wallet label{position:absolute;left:7px;font-size:11.5px;color:#555}
.wallet .field{position:absolute;left:70px;width:165px;height:22px;background:#fff;border:1px solid #bbb}
.login{left:70px;top:105px;width:83px;height:26px;border-radius:5px;background:linear-gradient(#ffd86a,#f2a60a);border:1px solid #c88800;font-size:14px;text-align:center;line-height:24px;color:#333}

/* footer */
.footer{left:0;top:1021px;width:1200px;height:57px;background:var(--footer);color:#fff;font-family:"Arimo",sans-serif;font-size:10px}
.footer-links{left:160px;top:13px;word-spacing:1px}
.footer-copy{left:160px;top:31px}
.rss{left:838px;top:20px;width:18px;height:18px;border-radius:3px;background:#f08a24}
.rss-label{left:860px;top:24px;color:#ccc;font-size:9.5px}
.rss-field{left:915px;top:21px;width:90px;height:17px;background:#fff}
.rss-go{left:1008px;top:21px;width:19px;height:17px;background:#8aa21d;font-size:8px;font-weight:bold;text-align:center;line-height:17px}
</style>
</head>
<body>

<header>
  <div class="abs brand"><span class="brand-mark"></span><span class="brand-name">quorvelbank</span></div>
  <div class="abs join">Join our network<span class="abs join-arrow"></span></div>
  <div class="abs social" aria-label="Social links"><span></span><span></span><span></span><span></span></div>
  <div class="abs nav-rule"></div>
  <nav class="abs nav">
    <a class="current" href="#">Home</a><a href="#">How to order</a><a href="#">Buy Gold</a><a href="#">Buy Silver</a><a href="#">About us</a><a href="#">FAQ</a>
  </nav>
</header>

<section class="abs hero">
  <div class="abs hero-art" role="img" aria-label="Stacked gold bars and coin piles"></div>
</section>
<h1 class="abs hero-title">Why Buy Gold?</h1>
<div class="abs hero-points">Gold has been rising for the past 10 years<br>protect your wealth in certain times<br>470% increase in value</div>
<div class="abs pay">
  <div class="abs pay-thumb" role="img" aria-label="Gold bars"></div>
  <div class="abs pay-small">Make a</div>
  <div class="abs pay-big">Payment On your Gold</div>
  <div class="abs pay-links">Enroll &nbsp; learn more at quorvelbank</div>
  <div class="abs pay-go"></div>
</div>

<svg class="abs arc" viewBox="0 0 1200 180" aria-hidden="true">
  <path d="M0 180 L0 166 L16 166 Q600 26 1184 164 L1200 164 L1200 180 Z" fill="var(--page)"/>
  <path d="M16 166 Q600 6 1184 164 Q600 26 16 166 Z" fill="var(--gold)"/>
  <g fill="#fff"><circle cx="577" cy="96" r="4.5"/><circle cx="595" cy="96" r="4.5"/><circle cx="613" cy="96" r="4.5"/><circle cx="631" cy="96" r="4.5"/></g>
</svg>

<section>
  <h2 class="abs about-title">About Us</h2>
  <p class="abs about-text" style="top:539px">Quorvelbank commenced trading in 2010 to eliminate counterparty risk for Irish investors who want to buy and sell precious metals. We offer low premiums and quick trade execution for large and small investors and most of our business comes through word of mouth referrals.</p>
  <p class="abs about-text" style="top:585px">Our prices are live and track changes in the underlying spot prices of the metals at 20 second intervals so you can be sure you are always getting the latest pricing on every order. We offer clients an unrivalled selection of bullion products in Ireland.</p>
  <div class="abs divider"></div>
  <div class="abs cta">Find out more about us</div>
</section>

<section>
  <div class="abs feat-bar">Quorvelbank &nbsp;// &nbsp;FEATURES
    <div class="abs feat-pager"><b></b><i class="on"></i><i></i><i></i></div>
  </div>
  <article class="abs card" style="left:158px">
    <div class="card-img" role="img" aria-label="Fine gold bars on dark red cloth" style="background:linear-gradient(135deg,#6b1010,#b8892e 45%,#e9c96a 60%,#4a0c0c)"></div>
    <h3>Sed do eiusmod tempor &nbsp;incidi dunt ut labore et dolore magna aliqua.</h3>
    <p>Lorem ipsum dolor sit amet, consectetur adipisicing elit, sed do eiusmod tempor incididunt ut labore et dolore magna aliqua.<br>Ut enim ad minim veniam, quis</p>
  </article>
  <article class="abs card" style="left:366px">
    <div class="card-img" role="img" aria-label="Row of polished gold bars" style="background:linear-gradient(160deg,#fff 0%,#f2d27a 35%,#c98f12 60%,#fff6dc 100%)"></div>
    <h3>Lorem ipsum dolor sit amet, con-sectetur adipisicing elit,<br>sed do eiusmod tempor</h3>
    <p>Lorem ipsum dolor sit amet, consecte-tur adipisicing elit, sed do eiusmod tempor incididunt ut labore et dolore magna aliqua.<br>Ut enim ad minim veniam, quis nostrud</p>
  </article>
  <article class="abs card" style="left:573px">
    <div class="card-img" role="img" aria-label="Gold bar with gold coins" style="background:linear-gradient(135deg,#7a4b06,#e3b24a 40%,#b57a10 70%,#f1cf7a)"></div>
    <h3>Lorem ipsum dolor sit amet, cons ectetur adipisic</h3>
    <p>Lorem ipsum dolor sit amet, con-sectetur adipisicing elit, sed do eiusmod tempor incididunt ut labore et dolore magna aliqua.<br>Ut enim ad minim veniam, quis nostrud exercitation.</p>
  </article>
</section>

<aside>
  <div class="abs promo">
    <h4>BUY SILVER</h4>
    <div class="abs offer">ON ORDERS OVER $</div>
    <div class="abs note">THIS OFFER IS VALID ON ALL<br>OUR &nbsp;STORE ITEMS</div>
    <div class="abs more">Read More</div>
    <div class="abs promo-art" role="img" aria-label="One ounce fine silver bars"></div>
  </div>
  <form class="abs wallet">
    <div class="wallet-head">E-Walltet</div>
    <label style="top:52px">Card #:</label><span class="field" style="top:46px"></span>
    <label style="top:85px">Account #:</label><span class="field" style="top:76px"></span>
    <div class="abs login">Login</div>
  </form>
</aside>

<footer class="abs footer">
  <div class="abs footer-links">Home &nbsp;- &nbsp;About &nbsp;- &nbsp;How to order &nbsp;- Buy Gold &nbsp;- Buy Silver &nbsp;- &nbsp;Services &nbsp;- &nbsp;Contacts &nbsp;- &nbsp;FAQ - &nbsp;Site Map &nbsp;-</div>
  <div class="abs footer-copy">Quorvelbank - All Rights Reserved.</div>
  <div class="abs rss"></div>
  <div class="abs rss-label">RSS - Email</div>
  <div class="abs rss-field"></div>
  <div class="abs rss-go">GO</div>
</footer>

</body>
</html>
```